Real Estate Web Design

I need someone who can design a few elements for a real estate website. I DO NOT need the whole website designed (though if you are good i might use you for that also)

The designs Needs to be done with CSS and HTML ONLY, with placeholders for images and property data (will be dynamically inserted). I need about 4-5 designs for the following: SINGLE property display, property listings displays (boxes, cards, list views etc), and property search forms. I also need the CSS to be THEME PROOF, meaning having unique class names that don't clash with any theme (this will eventually be used with Wordpress). The designs must also be FULLY RESPONSIVE.

If i pick your design, you also agree to any tweaks or adjustments that might be needed to make it fit/work with what i need. (like naming the classes etc)

I don't mind if you use or find a really cool existing design out there, so long as you adapt it to CSS and HTML ONLY. (and it doesn't violate any copyrights of course)

Thanks! Look forward to working with you!!

PS - i have added some screenshots from the VELTRA wordpress theme. These are elements i need. but i need them UNIQUE and i need them designed ONLY with HTML and css

```html
<!DOCTYPE html>
<html lang="en">
<head>
<meta charset="UTF-8">
<title>Property Listings</title>
<link href="https://fonts.googleapis.com/css2?family=Tinos:wght@400;700&family=Arimo:wght@400;700&display=swap" rel="stylesheet">
<style>
  :root {
    --topbar-grey: #6b6b6b;
    --topbar-text: #3c3c3c;
    --search-green: #008000;
    --pill-grey: #8a8a8a;
    --field-white: #ffffff;
    --field-text: #9a9a9a;
    --button-teal: #1f7f95;
    --button-edge: #6fb3c2;
    --heading-grey: #7b7b7b;
    --badge-red: #ff0000;
    --card-border: #a9a9a9;
    --ink: #111111;
    --price-green: #3aa84a;
    --page-bg: #ffffff;
  }
  * { box-sizing: border-box; margin: 0; padding: 0; }
  html, body {
    width: 1200px; height: 675px; overflow: hidden;
    background: var(--page-bg);
    font-family: "Tinos", "Times New Roman", serif;
  }
  .vx-page { width: 1200px; height: 675px; position: relative; overflow: hidden; }

  .vx-topbar {
    height: 45px; background: var(--topbar-grey);
    padding: 0 10px; display: flex; align-items: center;
  }
  .vx-topbar-title { font-size: 21px; font-weight: 700; color: var(--topbar-text); }

  .vx-search {
    height: 70px; background: var(--search-green);
    display: flex; align-items: center; gap: 14px;
  }
  .vx-search-label {
    width: 162px; height: 66px;
    background: var(--pill-grey); color: #fff;
    border-radius: 0 40px 40px 0;
    display: flex; align-items: center; justify-content: center;
    font-size: 18px; margin-right: 6px;
  }
  .vx-search-field {
    width: 153px; height: 32px; background: var(--field-white);
    border: 1px solid #cfcfcf; border-radius: 6px;
    font-size: 13px; color: var(--field-text);
    padding: 0 4px; display: flex; align-items: center;
  }
  .vx-search-button {
    width: 115px; height: 36px; background: var(--button-teal);
    color: #fff; border: 2px solid var(--button-edge); border-radius: 4px;
    font-family: "Arimo", sans-serif; font-size: 14px;
    display: flex; align-items: center; justify-content: center;
    margin-left: 4px;
  }

  .vx-section-title {
    font-size: 20px; font-weight: 700; color: var(--heading-grey);
    position: absolute; left: 57px; top: 132px;
  }

  .vx-listing {
    display: flex; gap: 14px;
    position: absolute; left: 27px; top: 216px;
  }
  .vx-card {
    width: 263px; height: 420px;
    border: 1px solid var(--card-border);
    position: relative; padding: 7px 4px 0 4px;
  }
  .vx-card-badge {
    position: absolute; left: -3px; top: 3px;
    background: var(--badge-red); color: #fff;
    font-size: 14px; line-height: 18px; padding: 1px 16px 2px; z-index: 2;
  }
  .vx-card-photo {
    height: 145px; width: 100%;
    background: linear-gradient(135deg, #c9c2b8 0%, #9c8a78 40%, #6f6a66 70%, #b8c7cf 100%);
  }
  .vx-card-name {
    font-family: "Arimo", sans-serif; font-weight: 700; font-size: 17px; line-height: 20px;
    text-align: center; color: var(--ink); margin-top: 32px;
  }
  .vx-card-text {
    font-size: 13.5px; line-height: 16px; text-align: center;
    color: var(--ink); margin: 17px 10px 0;
  }
  .vx-card-more {
    font-size: 17px; font-weight: 700; line-height: 20px; text-align: right;
    margin: 16px 12px 0 0; color: var(--ink);
  }
  .vx-card-actions {
    display: flex; justify-content: space-between; align-items: center;
    margin-top: 12px; padding-left: 28px;
  }
  .vx-card-buy {
    width: 115px; height: 36px; background: var(--button-teal);
    color: #fff; border: 2px solid var(--button-edge); border-radius: 4px;
    font-family: "Arimo", sans-serif; font-size: 14px;
    display: flex; align-items: center; justify-content: center;
  }
  .vx-card-price {
    width: 80px; height: 40px; background: var(--price-green);
    color: #fff; border-radius: 22px 0 0 22px;
    font-family: "Arimo", sans-serif; font-size: 14px;
    display: flex; align-items: center; justify-content: center;
  }
</style>
</head>
<body>
<div class="vx-page">
  <header class="vx-topbar">
    <span class="vx-topbar-title">property</span>
  </header>

  <form class="vx-search">
    <div class="vx-search-label">Property search</div>
    <div class="vx-search-field">Purpose</div>
    <div class="vx-search-field">Type</div>
    <div class="vx-search-field">Project</div>
    <div class="vx-search-field">Price Range</div>
    <div class="vx-search-field">No Of Badroom</div>
    <div class="vx-search-button">Search</div>
  </form>

  <h2 class="vx-section-title">our property</h2>

  <section class="vx-listing">
    <article class="vx-card">
      <span class="vx-card-badge">Available</span>
      <div class="vx-card-photo" role="img" aria-label="Photo of a bright open-plan living room"></div>
      <h3 class="vx-card-name">property name</h3>
      <p class="vx-card-text">property short discriptoin.property short discriptoin.property short discriptoin.property short discriptoin.property short discriptoin.</p>
      <p class="vx-card-more">Read More&gt;&gt;</p>
      <div class="vx-card-actions">
        <span class="vx-card-buy">Buy Now</span>
        <span class="vx-card-price">$900</span>
      </div>
    </article>
    <article class="vx-card">
      <span class="vx-card-badge">Available</span>
      <div class="vx-card-photo" role="img" aria-label="Photo of a bright open-plan living room"></div>
      <h3 class="vx-card-name">property name</h3>
      <p class="vx-card-text">property short discriptoin.property short discriptoin.property short discriptoin.property short discriptoin.property short discriptoin.</p>
      <p class="vx-card-more">Read More&gt;&gt;</p>
      <div class="vx-card-actions">
        <span class="vx-card-buy">Buy Now</span>
        <span class="vx-card-price">$900</span>
      </div>
    </article>
    <article class="vx-card">
      <span class="vx-card-badge">Available</span>
      <div class="vx-card-photo" role="img" aria-label="Photo of a bright open-plan living room"></div>
      <h3 class="vx-card-name">property name</h3>
      <p class="vx-card-text">property short discriptoin.property short discriptoin.property short discriptoin.property short discriptoin.property short discriptoin.</p>
      <p class="vx-card-more">Read More&gt;&gt;</p>
      <div class="vx-card-actions">
        <span class="vx-card-buy">Buy Now</span>
        <span class="vx-card-price">$900</span>
      </div>
    </article>
    <article class="vx-card">
      <span class="vx-card-badge">Available</span>
      <div class="vx-card-photo" role="img" aria-label="Photo of a bright open-plan living room"></div>
      <h3 class="vx-card-name">property name</h3>
      <p class="vx-card-text">property short discriptoin.property short discriptoin.property short discriptoin.property short discriptoin.property short discriptoin.</p>
      <p class="vx-card-more">Read More&gt;&gt;</p>
      <div class="vx-card-actions">
        <span class="vx-card-buy">Buy Now</span>
        <span class="vx-card-price">$900</span>
      </div>
    </article>
  </section>
</div>
</body>
</html>
```